Automotive Detailing Company looking for Billboard

We need a highway billboard designed. Our company is harbor gloss (www.harborgloss.ca). We want the billboard to have:

1. "harborgloss" as in the uploaded files, WITH the underline as shown

2. "harborgloss" must be large and about 30-40% of the billboard available space

3. Include KORVA and Glazeon Max logos on the billboard as these are the brands we use. Keep in mind we USE these brands and only are marketing that we USE them, and it is not a billboard to promote the brands beyond that we use them. The main thing we are marketing is "harborgloss"

4. Include "Fort McMurray" in the billboard. This billboard will be displayed approx. 250km from our business location.

5. Include mandatory key words "ceramic coating" "paint protection film" "undercarriage restoration" "polishing" "tint" "steam"

6. You can use one of our vehicle photos attached, however, it is not necessary and only provided for inspiration and an option

7. Include a small Chatterly and Snapgrid Logo

```html
<!DOCTYPE html>
<html lang="en">
<head>
<meta charset="utf-8">
<title>harborgloss — Fort McMurray Billboard</title>
<link rel="stylesheet" href="https://fonts.googleapis.com/css2?family=Barlow+Condensed:wght@400;500;600&family=Comfortaa:wght@500;600&display=swap">
<style>
  :root {
    --page: #cfcfcf;
    --carbon: #1b1a1e;
    --carbon-soft: #2a282e;
    --purple: #31254f;
    --purple-deep: #241c3a;
    --pink: #c54d98;
    --white: #ffffff;
    --ink: #2b2b2b;
    --black: #111111;
  }
  * { margin: 0; padding: 0; box-sizing: border-box; }
  html, body {
    width: 945px; height: 1200px; overflow: hidden;
    background: var(--page);
  }
  .billboard {
    position: absolute; left: 40px; top: 400px;
    width: 865px; height: 400px;
    background: linear-gradient(160deg, var(--carbon-soft), var(--carbon) 60%);
    overflow: hidden;
    box-shadow: 0 8px 18px rgba(0,0,0,.35);
  }
  .service-band {
    position: absolute; left: 0; top: 177px; width: 865px; height: 145px;
    background: linear-gradient(90deg, var(--purple) 0%, var(--purple) 48%, var(--purple-deep) 70%, var(--carbon) 100%);
  }
  .vehicle-photo {
    position: absolute; left: 410px; top: 40px; width: 455px; height: 300px;
    background: radial-gradient(ellipse 60% 55% at 60% 55%, #f3f4f6 0%, #d4d8de 45%, #9a9fa8 70%, rgba(40,40,46,0) 100%);
  }
  .wordmark {
    position: absolute; left: 18px; top: 6px;
    font-family: "Comfortaa", sans-serif; font-weight: 500;
    font-size: 92px; line-height: 1; letter-spacing: 0;
    color: var(--pink); white-space: nowrap;
  }
  .wordmark-rule {
    position: absolute; left: 22px; top: 101px; width: 330px; height: 6px;
    background: var(--pink);
  }
  .location {
    position: absolute; left: 20px; top: 120px;
    font-family: "Comfortaa", sans-serif; font-weight: 600;
    font-size: 37px; line-height: 1; color: var(--white); white-space: nowrap;
  }
  .services {
    position: absolute; list-style: none;
    font-family: "Barlow Condensed", sans-serif; font-weight: 400;
    font-size: 27px; line-height: 1; color: var(--white); white-space: nowrap;
  }
  .services li { position: relative; padding-left: 34px; }
  .services .tick { position: absolute; left: 0; top: 3px; width: 19px; height: 19px; }
  .services-left { left: 20px; top: 192px; }
  .services-left li { margin-bottom: 9px; }
  .services-left li.two-line { line-height: 0.82; margin-bottom: 8px; }
  .services-right { left: 282px; top: 192px; }
  .services-right li { margin-bottom: 9px; }
  .contact-strip {
    position: absolute; left: 0; top: 322px; width: 865px; height: 78px;
    background: var(--white);
  }
  .slash { position: absolute; left: 0; top: 0; width: 865px; height: 78px; }
  .phone {
    position: absolute; left: 22px; top: 18px;
    display: flex; align-items: center; gap: 10px;
    font-family: "Barlow Condensed", sans-serif; font-weight: 600;
    font-size: 38px; line-height: 1; color: var(--ink); white-space: nowrap;
  }
  .phone svg { width: 30px; height: 30px; }
  .divider {
    position: absolute; left: 288px; top: 12px; width: 2px; height: 52px;
    background: var(--pink);
  }
  .web-details {
    position: absolute; left: 312px; top: 17px; list-style: none;
    font-family: "Barlow Condensed", sans-serif; font-weight: 500;
    font-size: 17px; line-height: 1; color: var(--ink);
  }
  .web-details li { display: flex; align-items: center; gap: 9px; margin-bottom: 8px; }
  .web-details svg { width: 12px; height: 12px; }
  .socials {
    position: absolute; left: 452px; top: 36px; list-style: none;
    font-family: "Barlow Condensed", sans-serif; font-weight: 600;
    font-size: 11px; line-height: 1.15; color: var(--pink);
  }
  .partners {
    position: absolute; left: 555px; top: 0; width: 310px; height: 78px;
    font-family: "Barlow Condensed", sans-serif; color: var(--black);
  }
  .partner-korva { position: absolute; left: 22px; top: 22px; text-align: center; }
  .partner-korva .certified { display: block; font-weight: 600; font-size: 8px; letter-spacing: .3px; }
  .partner-korva .name { display: block; font-weight: 600; font-size: 26px; line-height: 1; }
  .partner-glazeon {
    position: absolute; left: 132px; top: 25px;
    display: flex; align-items: center; gap: 8px;
    font-weight: 600; font-size: 22px; line-height: 1;
  }
  .partner-glazeon .mark { width: 20px; height: 20px; background: var(--pink); }
</style>
</head>
<body>
  <main class="billboard">
    <div class="service-band"></div>
    <div class="vehicle-photo" role="img" aria-label="Photo of a white sports car with black wheels, front three-quarter view"></div>

    <h1 class="wordmark">harborgloss</h1>
    <div class="wordmark-rule"></div>
    <p class="location">Fort McMurray</p>

    <svg width="0" height="0" style="position:absolute">
      <defs>
        <symbol id="tick" viewBox="0 0 20 20">
          <path d="M17 9.5a7.5 7.5 0 1 1-3-6" fill="none" stroke="#c54d98" stroke-width="1.6" stroke-linecap="round"/>
          <path d="M6 9.5l3 3 8-8" fill="none" stroke="#c54d98" stroke-width="1.8" stroke-linecap="round" stroke-linejoin="round"/>
        </symbol>
      </defs>
    </svg>

    <ul class="services services-left">
      <li><svg class="tick"><use href="#tick"/></svg>Ceramic coating</li>
      <li class="two-line"><svg class="tick"><use href="#tick"/></svg>Undercarriage<br>restoration</li>
      <li><svg class="tick"><use href="#tick"/></svg>Paint protection film</li>
    </ul>
    <ul class="services services-right">
      <li><svg class="tick"><use href="#tick"/></svg>Polishing</li>
      <li><svg class="tick"><use href="#tick"/></svg>Tint</li>
      <li><svg class="tick"><use href="#tick"/></svg>Steam</li>
    </ul>

    <section class="contact-strip">
      <svg class="slash" viewBox="0 0 865 78" aria-hidden="true">
        <polygon points="549,0 556,0 530,78 523,78" fill="#111111"/>
      </svg>
      <div class="phone">
        <svg viewBox="0 0 24 24" aria-hidden="true">
          <path d="M6.6 3.5l2.6 3.6-1.7 2.2c1 2.2 2.9 4.2 5.2 5.3l2.2-1.7 3.6 2.6-1.3 3.2c-.3.6-1 .9-1.7.8C9.4 18.5 5.5 14.6 4.5 8.5c-.1-.7.2-1.4.8-1.7z" fill="#c54d98"/>
          <path d="M14 3.5a7 7 0 0 1 6.5 6.5M14 6.5a4 4 0 0 1 3.5 3.5" fill="none" stroke="#c54d98" stroke-width="1.6" stroke-linecap="round"/>
        </svg>
        <span>(780) 555 0142</span>
      </div>
      <div class="divider"></div>
      <ul class="web-details">
        <li>
          <svg viewBox="0 0 12 12" aria-hidden="true"><rect x="0.5" y="2" width="11" height="8" fill="#c54d98"/><path d="M0.5 2l5.5 4.5L11.5 2" fill="none" stroke="#fff" stroke-width="1"/></svg>
          info@harborgloss.ca
        </li>
        <li>
          <svg viewBox="0 0 12 12" aria-hidden="true"><circle cx="6" cy="6" r="5.5" fill="#c54d98"/><path d="M0.5 6h11M6 0.5c-2.4 3-2.4 8 0 11M6 0.5c2.4 3 2.4 8 0 11" fill="none" stroke="#fff" stroke-width=".8"/></svg>
          harborgloss.ca
        </li>
      </ul>
      <ul class="socials">
        <li>Chatterly</li>
        <li>Snapgrid</li>
      </ul>
      <div class="partners">
        <div class="partner-korva">
          <span class="certified">CERTIFIED INSTALLER</span>
          <span class="name">KORVA</span>
        </div>
        <div class="partner-glazeon">
          <span class="mark"></span>
          <span>Glazeon Max</span>
        </div>
      </div>
    </section>
  </main>
</body>
</html>
```